letter head for a construction company

Company Name: Zaviro Construction Limited

Address: Kilele Street, Tengeru Shores, Dar es salaam, Tanzania

Phone: 0754382916

email : info@zaviroconstruction.example

website : www.zaviroconstruction.example

```html
<!DOCTYPE html>
<html lang="en">
<head>
<meta charset="utf-8">
<title>Zaviro Construction Limited – Letterhead</title>
<link rel="stylesheet" href="https://fonts.googleapis.com/css2?family=Open+Sans:wght@400;600;700&display=swap">
<style>
  :root {
    --orange: #f07d1f;
    --ink: #2d2d30;
    --text: #3a3a3d;
    --muted: #6b6b70;
    --backdrop: #ececec;
    --paper: #ffffff;
  }
  * { box-sizing: border-box; margin: 0; padding: 0; }
  html, body {
    width: 1200px; height: 800px; overflow: hidden;
    background: var(--backdrop);
    font-family: "Open Sans", Arial, sans-serif;
    color: var(--text);
  }
  .letterhead {
    position: absolute; left: 330px; top: 18px;
    width: 540px; height: 764px;
    background: var(--paper);
    box-shadow: 0 2px 10px rgba(0,0,0,0.08);
    overflow: hidden;
  }
  .brand {
    position: absolute; left: 48px; top: 54px;
    display: flex; align-items: center; gap: 8px;
  }
  .brand-mark { width: 14px; height: 14px; background: var(--orange); }
  .brand-name {
    font-size: 17px; font-weight: 700; color: var(--ink);
    letter-spacing: 0.5px; text-transform: uppercase;
  }
  .letter-date {
    position: absolute; right: 48px; top: 108px;
    font-size: 9px; color: var(--text);
  }
  .sender {
    position: absolute; left: 72px; top: 116px;
    font-size: 8.5px; line-height: 13px;
  }
  .sender-name { color: var(--orange); font-weight: 600; font-size: 10px; }
  .sender-role { color: var(--muted); font-size: 7.5px; margin-bottom: 2px; }
  .sender-row { display: flex; gap: 6px; }
  .sender-key { color: var(--orange); font-weight: 700; width: 14px; }
  .sender-key.is-dark { color: var(--ink); }
  .letter-body {
    position: absolute; left: 72px; top: 224px; width: 400px;
    font-size: 9.2px; line-height: 16px;
  }
  .letter-body p + p { margin-top: 16px; }
  .signoff { position: absolute; left: 72px; top: 566px; }
  .signature {
    width: 120px; height: 34px; margin-bottom: 4px;
    background: linear-gradient(90deg, #f4f4f5, #ebebed);
    border-radius: 3px;
  }
  .signoff-name { font-size: 9.5px; font-weight: 700; color: var(--ink); }
  .signoff-role { font-size: 8.5px; color: var(--muted); }
  .footer {
    position: absolute; left: 72px; bottom: 36px;
    display: flex; align-items: center; gap: 30px;
    font-size: 9px; color: var(--ink);
  }
  .footer-item { display: flex; align-items: center; gap: 8px; }
  .footer-lines { line-height: 13px; }
  .footer-icon { width: 20px; height: 20px; flex: none; }
  .corner-decoration {
    position: absolute; right: 0; bottom: 0;
    width: 140px; height: 220px;
    background: linear-gradient(160deg, var(--orange) 0%, #c9692a 45%, var(--ink) 100%);
    clip-path: polygon(100% 0, 100% 100%, 0 100%, 30% 40%);
  }
</style>
</head>
<body>
  <main class="letterhead">
    <header class="brand">
      <span class="brand-mark"></span>
      <span class="brand-name">Zaviro Construction Limited</span>
    </header>

    <p class="letter-date">Date, 10 September, 2020</p>

    <section class="sender">
      <p class="sender-name">Daniel Mwita</p>
      <p class="sender-role">Chief Director</p>
      <p class="sender-row"><span class="sender-key">A :</span><span>Kilele Street, Tengeru Shores, Dar es salaam, Tanzania</span></p>
      <p class="sender-row"><span class="sender-key is-dark">W :</span><span>info@zaviroconstruction.example,<br>www.zaviroconstruction.example</span></p>
      <p class="sender-row"><span class="sender-key">P :</span><span>0754382916</span></p>
    </section>

    <article class="letter-body">
      <p>This is a sample letter that has been placed to demonstrate typing remat (Your Company). letterhead design. When positioned properly, it will serve to work in harmony with all other elements letterhead. This letterhead design is meant to project an image</p>
      <p>This letterhead design is meant project an image of professionalism reliability. By using simple aligen we have created a very spacious feeling. The simplicity suggest rengththe spaciousnes contributes h aesthetics the layout. These basic qualities along with the (Your Company)</p>
      <p>look and helps reinforce the (Your Company) brand. letterhead design is meant to project an image p design. When positioned properly, it will serve to work in harmony all the other elements letterhead. sionalism and reliability.</p>
      <p>This letterhead design is based on the (Form of your logo) form (Your Company) logo. Each stationery we have created a very spacious feeling. The simplicity suggests strength the spaciousnes contribute part of the (Form of your logo).</p>
    </article>

    <section class="signoff">
      <div class="signature" role="img" aria-label="Handwritten signature of Daniel Mwita"></div>
      <p class="signoff-name">Daniel Mwita</p>
      <p class="signoff-role">Manager</p>
    </section>

    <footer class="footer">
      <div class="footer-item">
        <svg class="footer-icon" viewBox="0 0 20 20" aria-hidden="true">
          <polygon points="0,4 20,0 16,20 0,16" fill="var(--orange)"/>
          <polygon points="20,0 16,20 6,20" fill="var(--ink)"/>
          <path d="M6 6 q1-1 2 0 l1 2 q0 1-1 1.5 q1 2 3 3 q0.5-1 1.5-1 l2 1 q1 1 0 2 q-2 2-5-0.5 q-3-2.5-4.5-5.5 q-1-2 1-2.5z" fill="#fff"/>
        </svg>
        <span>0754382916</span>
      </div>
      <div class="footer-item">
        <svg class="footer-icon" viewBox="0 0 20 20" aria-hidden="true">
          <polygon points="0,4 20,0 16,20 0,16" fill="var(--orange)"/>
          <polygon points="20,0 16,20 6,20" fill="var(--ink)"/>
          <circle cx="9.5" cy="10" r="4.5" fill="none" stroke="#fff" stroke-width="1.2"/>
          <line x1="5" y1="10" x2="14" y2="10" stroke="#fff" stroke-width="1"/>
          <ellipse cx="9.5" cy="10" rx="2" ry="4.5" fill="none" stroke="#fff" stroke-width="1"/>
        </svg>
        <span class="footer-lines">www.zaviroconstruction.example<br>info@zaviroconstruction.example</span>
      </div>
    </footer>

    <div class="corner-decoration" role="img" aria-label="Decorative cluster of orange, charcoal and grey triangles in the lower right corner"></div>
  </main>
</body>
</html>
```